Classic Personal Business Card in Regatta Dunmore Hale Style (Horizontal - Raised Ink)

If you ever seen a Dunmore Hale Regatta shirt, you will know that the signature of that shirt is small monogrammed icon on the left pocket. I envision my personal business card using some of these elements. I am in the oil exploration industry, which is very conservative and I want a card that looks great but still reflects that classic conservatism. I specifically do land management work, which means I determine who owns mineral rights, I lease those rights for larger companies to then drill for crude oil and natural gas

1. I have designed a small logo (which definitely could use some help) that I would like to be pretty small, centered in the middle of the card, and near the top of the card (color - navy blue or similar) Please feel free to make this logo infinitely better. However, I am not looking for anything abstract/

2. I want my name and designation (Marcus J. Thornbury, RPL) centered in the middle of the card. As far as font, I'm looking for a classic, strong (almost masculine) cursive font (I realize masculine + cursive is a little oxymoronic) and I would like it to the color to be Gold.

3. I would like my name (see above) to sit on top of a thin, centered navy blue (or similar) line as if it were almost a signature on a line. I want the lower-case letters that normally would dip below the line (which is y and p in my case) to do the same. I'll attach an example to help illustrate what I mean.

4. The rest of the card is my contact information. Because I am shoot for a more centered and balance look, I would like the placement of my contact information to also be centered and balance. Font should be a very classic, professional font. My first inclination is to use black for the color but I'm open to other suggestions.

Contact information:

Phone: (XXX) XXX-XXXX
Email: xxxxxxx@mailbox-example.net

Important Note: My hope is to have these printed with Raised Ink on High Quality High Quality Card Stock so it must conform to this Necessity.

Project Deadline Extended Reason: I am having major internet trouble. So I am not able to look at the submissions and provide feedback in a timely fashion. Also, it is difficult to access the site from just my phone. Added Saturday, November 22, 2014

Target Market(s)

US Oil Executives

Industry/Entity Type

Conservative

Contact Information for Business Card

I've posted a new logo that needs some clean up and a new idea for the top and bottom border of the card. I would like the logo to be centered in the top border with a white barrier on either side between the logo and the border. I've also posted color codes below.

Thanks

Requirements
Must have
• Color Codes:
• Blue: R - 0 G - 0 B - 102
• Gold R - 102 G - 102 B - 0

```html
<!DOCTYPE html>
<html lang="en">
<head>
<meta charset="utf-8">
<title>Marcus J. Thornbury R.P.L. – Business Card</title>
<link href="https://fonts.googleapis.com/css2?family=Anton&family=Architects+Daughter&display=swap" rel="stylesheet">
<style>
  :root {
    --navy: #0019a0;
    --gold: #f7cb15;
    --ink: #222222;
    --frame: #333333;
    --paper: #ffffff;
  }
  html, body {
    margin: 0;
    padding: 0;
    width: 1200px;
    height: 669px;
    overflow: hidden;
    background: var(--paper);
  }
  .card {
    position: relative;
    width: 1200px;
    height: 669px;
    box-sizing: border-box;
    border: 2px solid var(--frame);
    background: var(--paper);
  }
  .brand {
    position: absolute;
    left: 0;
    right: 0;
    top: 60px;
    display: flex;
    justify-content: center;
    align-items: center;
    gap: 18px;
  }
  .brand-mark {
    display: block;
  }
  .brand-name {
    font-family: "Anton", sans-serif;
    font-size: 34px;
    color: var(--navy);
    letter-spacing: 0.5px;
  }
  .signature {
    position: absolute;
    left: 220px;
    top: 272px;
    width: 760px;
    height: 80px;
  }
  .signature-line {
    position: absolute;
    left: 0;
    right: 0;
    top: 62px;
    height: 3px;
    background: var(--navy);
  }
  .signature-name {
    position: absolute;
    left: 0;
    right: 0;
    top: -8px;
    margin: 0;
    text-align: center;
    font-family: "Architects Daughter", cursive;
    font-weight: 400;
    font-size: 56px;
    line-height: 1.3;
    color: var(--gold);
    white-space: nowrap;
  }
  .contact {
    position: absolute;
    left: 0;
    right: 0;
    top: 500px;
    margin: 0;
    text-align: center;
    font-family: "Anton", sans-serif;
    font-size: 38px;
    line-height: 56px;
    color: var(--ink);
    font-style: normal;
  }
  .contact p { margin: 0; }
</style>
</head>
<body>
  <div class="card">
    <div class="brand">
      <svg class="brand-mark" width="64" height="64" viewBox="0 0 64 64" aria-hidden="true">
        <circle cx="32" cy="32" r="30" fill="none" stroke="var(--navy)" stroke-width="3"/>
      </svg>
      <span class="brand-name">Thornbury Land</span>
    </div>

    <div class="signature">
      <div class="signature-line"></div>
      <h1 class="signature-name">Marcus J. Thornbury R.P.L.</h1>
    </div>

    <address class="contact">
      <p>Phone: (XXX) XXX-XXXX</p>
      <p>Email: xxxxxxx@mailbox-example.net</p>
    </address>
  </div>
</body>
</html>
```